Business Card Revision

Need to redesign my business cards for a new professional look. We are a courier company. You can go to www.qvroutefast.com to see what we do. The trucks have an old company name (Nimble) on them but that is the company we are just now
changing the name.

Target Market(s)

Potential clients. We service the automotive, plumbing, printing, air freight industries as well as many others.

Industry/Entity Type

Business

Contact Information for Business Card

QVrushline
20583 Palmer Fenwick Parkway
Cincinnati, Oh 45317

Howard T. Lassiter
President

howie@qvroutefast.com

Main: (513) 555-0147

```html
<!DOCTYPE html>
<html lang="en">
<head>
<meta charset="utf-8">
<title>QVrushline Business Card</title>
<link rel="stylesheet" href="https://fonts.googleapis.com/css2?family=Arimo:wght@400;700&display=swap">
<style>
  :root {
    --brand-green: #3db54a;
    --brand-green-dark: #2fa33d;
    --brand-blue: #1a7bc4;
    --ink-grey: #6a6a6a;
    --rule-grey: #e2e2e2;
    --card-white: #ffffff;
    --stage: #ecebe8;
  }
  * { box-sizing: border-box; margin: 0; padding: 0; }
  html, body {
    width: 1200px; height: 950px; overflow: hidden;
    background: var(--stage);
    font-family: "Arimo", Arial, sans-serif;
  }
  .sheet {
    position: relative; width: 1200px; height: 950px;
    display: flex; flex-direction: column; align-items: center;
    justify-content: center; gap: 50px;
  }
  .card {
    position: relative; width: 700px; height: 400px; overflow: hidden;
    box-shadow: 0 6px 18px rgba(0,0,0,0.18);
  }
  .card-back {
    background: linear-gradient(135deg, var(--brand-green-dark), var(--brand-green) 60%, #46c153);
    display: flex; flex-direction: column; align-items: center; justify-content: center;
    color: var(--card-white);
  }
  .back-wordmark {
    font-weight: 700; font-size: 64px; letter-spacing: 1px;
  }
  .back-web {
    margin-top: 70px; font-size: 17px; letter-spacing: 4px;
  }
  .card-front { background: var(--card-white); }
  .front-shapes { position: absolute; inset: 0; }
  .front-wordmark {
    position: absolute; left: 40px; top: 240px;
    font-weight: 700; font-size: 44px; color: var(--brand-blue);
  }
  .contact {
    position: absolute; left: 430px; top: 70px;
    color: var(--ink-grey); font-size: 17px; line-height: 1.45;
  }
  .contact-name { color: var(--brand-blue); font-weight: 700; font-size: 25px; line-height: 1.2; }
  .contact-title { color: var(--brand-green); font-size: 18px; margin-bottom: 12px; }
  .contact-address { margin-bottom: 6px; }
  .contact-line { display: flex; align-items: center; gap: 8px; }
  .contact-line svg { width: 16px; height: 16px; flex: none; }
</style>
</head>
<body>
<main class="sheet">
  <section class="card card-back" aria-label="Card back">
    <div class="back-wordmark">QV Routefast</div>
    <div class="back-web">www.qvroutefast.com</div>
  </section>

  <section class="card card-front" aria-label="Card front">
    <svg class="front-shapes" viewBox="0 0 700 400" aria-hidden="true">
      <polygon points="0,0 640,0 0,58" fill="var(--brand-blue)"/>
      <line x1="360" y1="25" x2="470" y2="400" stroke="var(--rule-grey)" stroke-width="1.5"/>
      <polygon points="240,400 700,285 700,400" fill="var(--brand-green)"/>
    </svg>

    <div class="front-wordmark">QV Routefast</div>

    <div class="contact">
      <div class="contact-name">Howard T. Lassiter</div>
      <div class="contact-title">President</div>
      <div class="contact-address">QVrushline<br>20583 Palmer Fenwick Parkway<br>Cincinnati, Oh 45317</div>
      <div class="contact-line">
        <svg viewBox="0 0 16 16"><path d="M3 2h3l1 4-2 1a8 8 0 0 0 4 4l1-2 4 1v3a1 1 0 0 1-1 1A12 12 0 0 1 2 3a1 1 0 0 1 1-1z" fill="var(--brand-blue)"/></svg>
        <span>(513) 555-0147</span>
      </div>
      <div class="contact-line">
        <svg viewBox="0 0 16 16"><rect x="1" y="3" width="14" height="10" rx="1" fill="var(--brand-blue)"/><path d="M1.5 4l6.5 5 6.5-5" stroke="#fff" stroke-width="1.3" fill="none"/></svg>
        <span>howie@qvroutefast.com</span>
      </div>
      <div class="contact-line">
        <svg viewBox="0 0 16 16"><circle cx="8" cy="8" r="7" fill="var(--brand-blue)"/><path d="M1 8h14M8 1c-3 3-3 11 0 14M8 1c3 3 3 11 0 14" stroke="#fff" stroke-width="1" fill="none"/></svg>
        <span>www.qvroutefast.com</span>
      </div>
    </div>
  </section>
</main>
</body>
</html>
```